Certified Public Accountant specializing in tax preparation.

I need a business card designed that conveys knowledgeability, trustworthiness and competency. I am a licensed CPA and hold a Master's in taxation. As this is a personal service business, I would like to include my picture on the card.

```html
<!DOCTYPE html>
<html lang="en">
<head>
<meta charset="utf-8">
<title>CPA Business Card</title>
<link rel="stylesheet" href="https://fonts.googleapis.com/css2?family=Raleway:wght@400;500;700&display=swap">
<style>
  :root {
    --page-bg: #ffffff;
    --card-dark: #071720;
    --band-pink: #ec008c;
    --stripe-white: #ffffff;
    --stripe-grey-light: #c4c6c8;
    --stripe-grey-dark: #8c8e91;
    --purple-light: #c1128a;
    --purple-mid: #95178e;
    --purple-deep: #5f1e8a;
    --text-light: #ffffff;
  }
  html, body {
    margin: 0;
    padding: 0;
    width: 1200px;
    height: 1200px;
    overflow: hidden;
    background: var(--page-bg);
  }
  .canvas {
    display: block;
    width: 1200px;
    height: 1200px;
  }
  .card-name {
    font-family: "Raleway", sans-serif;
    font-weight: 700;
    font-size: 58px;
    letter-spacing: 4px;
    fill: var(--text-light);
  }
  .card-title {
    font-family: "Raleway", sans-serif;
    font-weight: 400;
    font-size: 37px;
    fill: var(--text-light);
  }
  .card-contact {
    font-family: "Raleway", sans-serif;
    font-weight: 500;
    font-size: 32px;
    fill: var(--text-light);
  }
  .icon { fill: var(--text-light); }
  .portrait-ring { fill: none; stroke: var(--text-light); stroke-width: 3; }
</style>
</head>
<body>
<svg class="canvas" viewBox="0 0 1500 1500" xmlns="http://www.w3.org/2000/svg">
  <defs>
    <radialGradient id="purpleGlow" cx="430" cy="610" r="520" gradientUnits="userSpaceOnUse">
      <stop offset="0" stop-color="var(--purple-light)"/>
      <stop offset="0.55" stop-color="var(--purple-mid)"/>
      <stop offset="1" stop-color="var(--purple-deep)"/>
    </radialGradient>
    <linearGradient id="greyStripe" x1="0" y1="0" x2="1" y2="1">
      <stop offset="0" stop-color="var(--stripe-grey-dark)"/>
      <stop offset="0.5" stop-color="var(--stripe-grey-light)"/>
      <stop offset="1" stop-color="var(--stripe-grey-dark)"/>
    </linearGradient>
    <linearGradient id="bandFade" x1="650" y1="0" x2="800" y2="0" gradientUnits="userSpaceOnUse">
      <stop offset="0" stop-color="var(--band-pink)" stop-opacity="0.6"/>
      <stop offset="1" stop-color="var(--band-pink)"/>
    </linearGradient>
    <radialGradient id="portraitTone" cx="0.5" cy="0.45" r="0.6">
      <stop offset="0" stop-color="#d9a98f"/>
      <stop offset="0.5" stop-color="#8a5a45"/>
      <stop offset="1" stop-color="#b7795a"/>
    </radialGradient>
    <clipPath id="cardClip">
      <rect x="228" y="410" width="1045" height="680"/>
    </clipPath>
  </defs>

  <g class="business-card" clip-path="url(#cardClip)">
    <rect class="card-base" x="228" y="410" width="1045" height="680" fill="var(--card-dark)"/>

    <polygon class="stripe-white" points="228,410 645,410 820,680 444,1090 228,1090" fill="var(--stripe-white)"/>
    <polygon class="stripe-grey" points="228,410 605,410 780,680 403,1090 228,1090" fill="url(#greyStripe)"/>

    <rect class="name-band" x="650" y="592" width="623" height="188" fill="url(#bandFade)"/>

    <path class="photo-panel" d="M228,410 L563,410 L705,625 Q725,660 702,695 L362,1090 L228,1090 Z" fill="url(#purpleGlow)"/>

    <circle class="portrait-photo" cx="438" cy="690" r="130" fill="url(#portraitTone)" role="img" aria-label="Portrait photo of the accountant"/>
    <circle class="portrait-ring" cx="438" cy="690" r="131"/>

    <text class="card-name" x="1213" y="691" text-anchor="end">Name Surname</text>
    <text class="card-title" x="1212" y="743" text-anchor="end">CPA and Master's in taxation</text>

    <text class="card-contact" x="1155" y="839" text-anchor="end">companyname@mail.com</text>
    <text class="card-contact" x="1143" y="894" text-anchor="end">your street, 88</text>
    <text class="card-contact" x="1143" y="945" text-anchor="end">111-222-333-444</text>

    <path class="icon icon-pin" d="M1182,812 a16,16 0 0 1 16,16 c0,12 -16,26 -16,26 c0,0 -16,-14 -16,-26 a16,16 0 0 1 16,-16 z M1182,822 a6,6 0 1 0 0.01,0 z" fill-rule="evenodd"/>

    <g class="icon icon-mail">
      <rect x="1163" y="873" width="37" height="26" rx="2"/>
      <polyline points="1165,876 1181.5,890 1198,876" fill="none" stroke="var(--card-dark)" stroke-width="3"/>
    </g>

    <path class="icon icon-phone" d="M1170,918 l7,-2 l6,11 l-5,4 c2,5 6,9 11,11 l4,-5 l11,6 l-2,7 c-2,3 -6,4 -10,3 c-12,-4 -21,-13 -25,-25 c-1,-4 0,-8 3,-10 z"/>
  </g>
</svg>
</body>
</html>
```